TK AG Flyer design

I’d like to redesign an A5, double-sided flyer for the company TK AG (www.tkag.lu). The text/content is available in a Word document.

```html
<!DOCTYPE html>
<html lang="de">
<head>
<meta charset="utf-8">
<title>TK AG Flyer A5</title>
<link href="https://fonts.googleapis.com/css2?family=Poppins:wght@400;500;600;700;800&family=Barlow+Condensed:wght@700&display=swap" rel="stylesheet">
<style>
:root{
  --navy:#0c0a86;
  --orange:#f7a04a;
  --ink:#2b2b33;
  --muted:#55555f;
  --bar:#e7e8eb;
  --paper:#ffffff;
  --stage:#efeff0;
}
*{box-sizing:border-box;margin:0;padding:0}
html,body{width:1200px;height:759px;overflow:hidden;background:var(--stage);font-family:'Poppins',sans-serif;color:var(--ink)}
.spread{position:relative;width:1200px;height:759px;display:flex;justify-content:center;align-items:center;gap:80px}
.page{position:relative;width:480px;height:683px;background:var(--paper);display:flex;flex-direction:column;box-shadow:0 10px 30px rgba(0,0,0,.18)}

/* brand: plain name with one square */
.brand{display:flex;align-items:center;gap:10px}
.brand-mark{width:26px;height:26px;background:var(--navy)}
.brand-name{font-weight:700;color:var(--navy);line-height:1}

/* front header */
.front-head{height:106px;display:flex;align-items:center;justify-content:center}
.front-head .brand-mark{width:30px;height:30px}
.front-head .brand-name{font-size:32px}

/* hero */
.hero{position:relative;height:242px;overflow:hidden}
.hero-photo{position:absolute;inset:0;background:linear-gradient(100deg,#7fa7d8 0%,#3c5aa6 40%,#c4c4c8 58%,#bfbfc4 100%)}
.hero-fade{position:absolute;inset:0;background:linear-gradient(180deg,rgba(12,10,134,0) 25%,rgba(12,10,134,.75) 60%,var(--navy) 100%)}
.hero-copy{position:absolute;left:0;right:0;top:114px;text-align:center;color:#fff}
.hero-title{font-weight:800;font-size:31px;line-height:1.02;letter-spacing:-.01em}
.hero-sub{font-size:13px;font-weight:400;margin-top:3px;letter-spacing:.03em}
.dot-rule{position:relative;height:2px;background:currentColor;margin:0 auto}
.dot-rule::before,.dot-rule::after{content:"";position:absolute;top:-2px;width:6px;height:6px;border-radius:50%;background:currentColor}
.dot-rule::before{left:-2px}.dot-rule::after{right:-2px}
.hero .dot-rule{width:160px;margin-top:9px;height:1.5px}
.hero-claims{margin-top:12px;font-size:8px;color:var(--orange);letter-spacing:.02em}
.hero-claims span{margin:0 6px}

/* front body */
.front-body{position:relative;height:235px;padding:17px 38px 0}
.intro{font-size:7.6px;color:var(--muted)}
.label{display:inline-block;margin-top:10px;padding:4px 26px 4px 11px;font-size:10px;color:#fff;clip-path:polygon(0 0,100% 0,90% 100%,0 100%)}
.label b{font-weight:700}
.label-navy{background:var(--navy)}
.label-orange{background:var(--orange)}
.lead{font-size:7.6px;font-weight:600;margin-top:7px}
.ticks{list-style:none;margin-top:5px;padding-left:15px;position:relative}
.ticks::before{content:"";position:absolute;left:7px;top:4px;bottom:4px;width:1px;background:#9a9aa3}
.ticks li{position:relative;font-size:7.6px;line-height:1.55;color:var(--muted)}
.ticks li::before{content:"";position:absolute;left:-10px;top:4.5px;width:3.5px;height:3.5px;border-radius:50%;background:#7a7a83}
.ticks b{font-weight:600;color:var(--ink)}
.cta{position:absolute;right:30px;bottom:-10px;width:110px;height:110px;border-radius:50%;background:var(--navy);color:#fff;text-align:center;display:flex;flex-direction:column;justify-content:center;align-items:center;z-index:2}
.cta-title{font-weight:700;font-size:10.5px;line-height:1.02}
.cta-note{margin-top:6px;font-size:4.6px;font-weight:600;color:var(--orange);line-height:1.25;width:76px}

/* member bar + footer */
.member-bar{height:31px;background:var(--bar);display:flex;justify-content:space-between;align-items:center;padding:0 38px 0 42px}
.member-text{font-size:5.4px;color:#4a4a52;line-height:1.5}
.member-text b{font-weight:500;color:var(--ink)}
.partners{text-align:right}
.partner-row{display:flex;gap:10px;justify-content:flex-end}
.partner{height:9px;background:#3d3d46;border-radius:1px}
.partner.a{width:62px}.partner.b{width:62px;background:#7b7b84}
.legal{font-size:5px;color:#5a5a63;margin-top:2px}
.footer{flex:1;background:var(--navy);display:flex;justify-content:space-between;align-items:center;padding:0 40px 0 42px;color:#fff}
.phone{display:flex;align-items:center;gap:7px;font-family:'Barlow Condensed',sans-serif;font-weight:700;font-size:24px;letter-spacing:.01em}
.address{font-size:7.6px;text-align:right;line-height:1.55}

/* back */
.back-body{height:468px;padding:44px 38px 0}
.back-top{display:flex;justify-content:space-between;align-items:flex-start}
.back-title{font-weight:800;font-size:30px;line-height:.95;color:var(--navy);letter-spacing:-.01em}
.back-sub{font-size:11px;color:var(--orange);margin-top:8px}
.back-top .brand{gap:6px;margin-top:8px}
.back-top .brand-mark{width:16px;height:16px}
.back-top .brand-name{font-size:12px}
.back-body .dot-rule{width:100%;height:1px;color:#444;margin-top:12px}
.copy{font-size:7.3px;line-height:1.6;color:var(--muted)}
.copy b{font-weight:600;color:var(--ink)}
.copy.first{margin-top:15px}
.section-head{font-size:11px;font-weight:500;color:var(--ink);margin-top:17px;margin-bottom:6px}
.steps{list-style:none;padding-left:22px;position:relative}
.steps::before{content:"";position:absolute;left:13px;top:4px;bottom:4px;width:1px;background:var(--orange)}
.steps li{position:relative;font-size:7.4px;line-height:1.55;color:var(--muted)}
.steps li::before{content:"";position:absolute;left:-10.5px;top:4.5px;width:3.5px;height:3.5px;border-radius:50%;background:var(--orange)}
.steps b{font-weight:600;color:var(--ink)}
.back-photo{height:114px;background:linear-gradient(100deg,#33478f 0%,#6a86c3 35%,#b9a57a 65%,#8aa0b8 100%)}
</style>
</head>
<body>
<main class="spread">

  <section class="page page-front">
    <header class="front-head">
      <div class="brand">
        <span class="brand-mark"></span>
        <span class="brand-name">TK AG</span>
      </div>
    </header>

    <div class="hero">
      <div class="hero-photo" role="img" aria-label="Foto eines Hausdachs mit Solarmodulen vor Hügellandschaft, rechts Schnittgrafik eines Hauses mit Haustechnik"></div>
      <div class="hero-fade"></div>
      <div class="hero-copy">
        <h1 class="hero-title">SOLAR ENERGIE &amp;<br>ENERGIE EFFIZIENZ</h1>
        <p class="hero-sub">AUS EINER HAND</p>
        <div class="dot-rule"></div>
        <p class="hero-claims">MEHR EIGENVERBRAUCH<span>•</span>MEHR EFFIZIENZ<span>•</span>MEHR ZUKUNFT</p>
      </div>
    </div>

    <div class="front-body">
      <p class="intro">Wir planen und beraten rund um Photovoltaik und Energieeffizienz – für Private, Gewerbe und Industrie.</p>

      <div class="label label-navy"><b>SOLAR</b> ENERGIE</div>
      <p class="lead">Photovoltaik-Lösungen, die zu Ihrem Dach passen</p>
      <ul class="ticks">
        <li><b>Indach PV-Anlagen</b> (integriert &amp; ästhetisch)</li>
        <li><b>Aufdach PV-Anlagen</b> (effizient &amp; preis-/leistungsstark)</li>
        <li><b>Eigenverbrauch optimieren</b> (Batterie, Wärmepumpe, E-Mobility, smartes Lastmanagement)</li>
      </ul>

      <div class="label label-orange"><b>ENERGIE</b> EFFIZIENZ</div>
      <p class="lead">Beratung &amp; Konzepte für nachhaltige Gebäude</p>
      <ul class="ticks">
        <li><b>Energieberatung / GEAK / GEAK Plus</b></li>
        <li><b>Impulsberatung &amp; Energiekonzept</b> (HLK + PV, Simulationen, Nachweise)</li>
        <li><b>Energiesanierung</b> (Planung, Koordination, Förderabwicklung)</li>
      </ul>

      <div class="cta">
        <div class="cta-title">Jetzt<br>unverbindlich<br>Kontakt<br>aufnehmen</div>
        <div class="cta-note">TELEFON ODER E-MAIL – WIR MELDEN UNS ZEITNAH.</div>
      </div>
    </div>

    <div class="member-bar">
      <div class="member-text"><b>Mitglied der Firmengruppe</b><br>Netzhaus Luzern AG – Netzwerk I Kompetenz I Innovation</div>
      <div class="partners">
        <div class="partner-row"><span class="partner a"></span><span class="partner b"></span></div>
        <div class="legal">Datenschutz | Impressum</div>
      </div>
    </div>

    <footer class="footer">
      <div class="phone">
        <svg width="12" height="20" viewBox="0 0 12 20" aria-hidden="true"><rect x="1" y="1" width="10" height="18" rx="2" fill="none" stroke="#f7a04a" stroke-width="1.6"/><line x1="4.5" y1="16" x2="7.5" y2="16" stroke="#f7a04a" stroke-width="1.4"/></svg>
        +41 41 555 0142
      </div>
      <div class="address">Mattenweg 12, CH-6003 Luzern<br>www.tkag.lu &nbsp;|&nbsp; info@tkag.lu</div>
    </footer>
  </section>

  <section class="page page-back">
    <div class="back-body">
      <div class="back-top">
        <div>
          <h2 class="back-title">Indach oder<br>Aufdach?</h2>
          <p class="back-sub">WIR FINDEN DIE PASSENDE LÖSUNG.</p>
        </div>
        <div class="brand">
          <span class="brand-mark"></span>
          <span class="brand-name">TK AG</span>
        </div>
      </div>
      <div class="dot-rule"></div>

      <p class="copy first"><b>Indach PV</b> ist ideal bei Neubau oder Dachsanierung: Module ersetzen die Dacheindeckung – funktional und optisch hochwertig.<br><b>Aufdach PV</b> eignet sich besonders bei bestehenden Dächern in gutem Zustand – mit Standardmodulen oft die effizienteste Technologie zum besten Preis.</p>

      <h3 class="section-head">Eigenverbrauch erhöhen – Rendite steigern</h3>
      <p class="copy">Viele PV-Anlagen produzieren mehr Strom, als gleichzeitig benötigt wird. Mit passenden Massnahmen erhöhen Sie Ihren Eigenverbrauch – z. B. durch <b>Batteriesysteme, Wärmepumpen-Ansteuerung, überschussvariables Laden von E-Fahrzeugen</b> oder gezieltes Schalten von Verbrauchern.</p>

      <h3 class="section-head">Energieberatung &amp; Sanierung – ganzheitlich gedacht</h3>
      <p class="copy">Wir analysieren Ihr Gebäude, erstellen einen <b>Sanierungs- und Effizienzplan</b> und unterstützen bei <b>Bewilligungen und Fördergeldern</b> – bis zur Umsetzung und Abnahme.</p>

      <h3 class="section-head">So läuft die Zusammenarbeit</h3>
      <ul class="steps">
        <li><b>Erstkontakt</b> (Telefon/E-Mail)</li>
        <li><b>Analyse / Check vor Ort</b> (Daten, Bedarf, Potenziale)</li>
        <li><b>Konzept, Wirtschaftlichkeit &amp; Massnahmenplan</b></li>
        <li><b>Umsetzung</b> mit eingespieltem Partnernetzwerk</li>
        <li>Optional: <b>Monitoring &amp; Wartung</b> für dauerhaft hohe Leistung</li>
      </ul>
    </div>

    <div class="back-photo" role="img" aria-label="Foto eines Schrägdachs mit dunklen Solarmodulen und Baugerüst vor herbstlicher Hügellandschaft"></div>

    <div class="member-bar">
      <div class="member-text"><b>Mitglied der Firmengruppe</b><br>Netzhaus Luzern AG – Netzwerk I Kompetenz I Innovation</div>
      <div class="partners">
        <div class="partner-row"><span class="partner a"></span><span class="partner b"></span></div>
        <div class="legal">Datenschutz | Impressum</div>
      </div>
    </div>

    <footer class="footer">
      <div class="phone">
        <svg width="12" height="20" viewBox="0 0 12 20" aria-hidden="true"><rect x="1" y="1" width="10" height="18" rx="2" fill="none" stroke="#f7a04a" stroke-width="1.6"/><line x1="4.5" y1="16" x2="7.5" y2="16" stroke="#f7a04a" stroke-width="1.4"/></svg>
        +41 41 555 0142
      </div>
      <div class="address">Mattenweg 12, CH-6003 Luzern<br>www.tkag.lu &nbsp;|&nbsp; info@tkag.lu</div>
    </footer>
  </section>

</main>
</body>
</html>
```